2in1 Bartender & Sommelier needs a business card

I need a business card. I worked as a bartender in many places but I just finished a sommelier school and I would like a new business card. I like minimal design, natural materials and something what makes the people think :) I try to be creative in cocktail making, like little mixology, little twist on recipes... I like to travel and discover new places, cultures and of course interesting drinks and improve continously...live a little bit crazy life. And I like what I do...

Target Market(s)

restaurant/winebar managers, winemakers, other sommeliers and bartenders, people who work in food and beverage sector

Industry/Entity Type

Hospitality

Contact Information for Business Card

Rozsa Tarkany
Bartender & Sommelier
Phone: (FR) +33 6 4827 3190
(HU) +36 70 918 6352

Font styles to use
Script

Requirements
Must have
• Some sign, I am a bartender and sommelier as well.
Nice to have
• black and white maybe with 1 or 2 extra color
Should not have
• very colourful, to many things on the card

```html
<!DOCTYPE html>
<html lang="en">
<head>
<meta charset="UTF-8">
<title>Rozsa Tarkany – Bartender &amp; Sommelier</title>
<link rel="stylesheet" href="https://fonts.googleapis.com/css2?family=Montserrat:wght@400;800&display=swap">
<style>
  :root {
    --page: #d9dfe2;
    --card: #e8edef;
    --ink: #1c1c1e;
    --night: #1d1d1f;
    --amber: #f0a823;
    --paper: #ffffff;
    --icon-disc: #cfdde0;
    --glass: #8a8d90;
  }
  * { margin: 0; padding: 0; box-sizing: border-box; }
  html, body {
    width: 1200px; height: 900px; overflow: hidden;
    background: var(--page);
    font-family: "Montserrat", sans-serif;
  }
  .card {
    position: absolute; left: 226px; top: 237px;
    width: 748px; height: 425px;
    background: var(--card);
    overflow: hidden;
    box-shadow: 0 6px 24px rgba(0,0,0,.12);
  }
  .night-band {
    position: absolute; left: 0; top: 232px;
    width: 100%; height: 193px;
    background: var(--night);
  }
  .bar-shelf {
    position: absolute; left: 75px; top: 70px;
    width: 262px; height: 77px;
    background: linear-gradient(180deg, rgba(138,141,144,0) 0%, rgba(138,141,144,.35) 50%, rgba(40,40,42,.7) 100%);
  }
  .name-panel {
    position: absolute; left: 65px; top: 147px;
    width: 282px; height: 170px;
    background: var(--card);
    border: 10px solid var(--night);
    display: flex; flex-direction: column; justify-content: center;
    padding-left: 26px;
  }
  .name-panel span {
    display: block;
    font-weight: 800; font-size: 40px; line-height: 1.1;
    letter-spacing: 1px; color: var(--ink);
    white-space: nowrap;
  }
  .amber-bar {
    position: absolute; left: 75px; top: 330px;
    width: 263px; height: 22px;
    background: var(--amber);
  }
  .identity {
    position: absolute; left: 397px; top: 162px;
    color: var(--ink);
  }
  .identity .full-name {
    font-weight: 800; font-size: 27px; letter-spacing: .5px; line-height: 1.2;
  }
  .identity .role {
    font-weight: 400; font-size: 21px; line-height: 1.3;
  }
  .contacts {
    position: absolute; left: 400px; top: 266px;
    list-style: none; color: var(--paper);
  }
  .contacts li {
    display: flex; align-items: center;
    height: 30.5px; font-size: 19px; letter-spacing: .3px;
    white-space: nowrap;
  }
  .contacts svg { width: 24px; height: 24px; margin-right: 17px; flex: none; }
</style>
</head>
<body>
  <div class="card">
    <div class="night-band"></div>
    <div class="bar-shelf" role="img" aria-label="Row of cocktail glasses, wine bottles and tumblers standing on the logo frame"></div>
    <div class="name-panel">
      <span>ROZSA</span>
      <span>TARKANY</span>
    </div>
    <div class="amber-bar"></div>

    <div class="identity">
      <div class="full-name">ROZSA TARKANY</div>
      <div class="role">Bartender &amp; Sommelier</div>
    </div>

    <ul class="contacts">
      <li>
        <svg viewBox="0 0 24 24" aria-hidden="true"><circle cx="12" cy="12" r="12" fill="var(--icon-disc)"/><path d="M6 10c0-2 2.5-3 6-3s6 1 6 3v1h-3v-1.5h-6V11H6z M8 12h8l1.5 5h-11z" fill="var(--night)"/><circle cx="12" cy="14.5" r="1.4" fill="var(--icon-disc)"/></svg>
        (FR) +33 6 4827 3190
      </li>
      <li>
        <svg viewBox="0 0 24 24" aria-hidden="true"><circle cx="12" cy="12" r="12" fill="var(--icon-disc)"/><path d="M6 10c0-2 2.5-3 6-3s6 1 6 3v1h-3v-1.5h-6V11H6z M8 12h8l1.5 5h-11z" fill="var(--night)"/><circle cx="12" cy="14.5" r="1.4" fill="var(--icon-disc)"/></svg>
        (HU) +36 70 918 6352
      </li>
      <li>
        <svg viewBox="0 0 24 24" aria-hidden="true"><circle cx="12" cy="12" r="12" fill="var(--icon-disc)"/><rect x="6" y="8" width="12" height="8.5" rx="1" fill="var(--night)"/><path d="M6.5 8.8 12 13l5.5-4.2" fill="none" stroke="var(--icon-disc)" stroke-width="1.2"/></svg>
        rtarkany@pourmail.com
      </li>
    </ul>
  </div>
</body>
</html>
```